The Copper Lantern Business Cards

We are a Craft Beer/Upscale dining Bar/Restaurant. We'll have 24 taps of craft beers and several types of bottled beers. In addition, we'll be serving a variety of top shelf bourbons, spirits and wines with a small unique menu. I'd like the design to be sophisticated, elegant and modern while staying away from "cartoonish" pictures.
Updates
Hello, I've added some example logos for inspiration. I'd like to use a lot of black/white with maybe a little color for a "pop". Thank you!
Industry/Entity Type
Business
Contact Information for Business Card
THE COPPER LANTERN
Marco Dellarosa
592 Wexley Street
Norfolk, Virginia 23847
Office: (757) 555-0148
Mobile: (757) 555-0193
Look and feel

```html
<!DOCTYPE html>
<html lang="en">
<head>
<meta charset="utf-8">
<title>The Copper Lantern – Business Card</title>
<link rel="stylesheet" href="https://fonts.googleapis.com/css2?family=Inter:wght@300;400&display=swap">
<style>
  :root {
    --page-bg: #e4e1dd;
    --card-black: #0b0b0b;
    --card-glow: #2a2a2a;
    --silver: #f2f2f2;
    --silver-soft: #cfcfcf;
    --frame: #bdbdbd;
  }
  html, body {
    margin: 0;
    padding: 0;
    width: 1200px;
    height: 1200px;
    overflow: hidden;
    background: var(--page-bg);
  }
  .canvas {
    position: relative;
    width: 1200px;
    height: 1200px;
  }
  .business-card {
    position: absolute;
    left: 280px;
    top: 53px;
    width: 640px;
    height: 1094px;
    background: radial-gradient(ellipse 70% 45% at 50% 45%, var(--card-glow), var(--card-black) 85%);
    box-shadow: 0 6px 24px rgba(0,0,0,0.25);
    font-family: "Inter", "Helvetica Neue", Arial, sans-serif;
    color: var(--silver);
    text-align: center;
  }
  .card-frame {
    position: absolute;
    inset: 14px;
    border: 2px solid var(--frame);
    pointer-events: none;
  }
  .brand-name {
    position: absolute;
    left: 0;
    right: 0;
    top: 232px;
    margin: 0;
    font-size: 40px;
    font-weight: 300;
    letter-spacing: 1px;
    color: var(--silver);
  }
  .contact-block {
    position: absolute;
    left: 0;
    right: 0;
    top: 600px;
  }
  .person-name {
    margin: 0;
    font-size: 54px;
    font-weight: 300;
    line-height: 1.1;
    letter-spacing: 0.5px;
  }
  .divider {
    height: 2px;
    background: var(--silver-soft);
    margin: 0 auto;
  }
  .divider--wide { width: 496px; margin-top: 14px; }
  .divider--narrow { width: 384px; margin-top: 12px; }
  .address {
    margin: 12px 0 0;
    font-style: normal;
    font-size: 32px;
    font-weight: 300;
    line-height: 48px;
  }
  .phones {
    margin: 14px 0 0;
    font-size: 32px;
    font-weight: 300;
    line-height: 48px;
  }
  .tagline {
    position: absolute;
    left: 0;
    right: 0;
    top: 970px;
    margin: 0;
    font-size: 22px;
    font-weight: 400;
    line-height: 37px;
    letter-spacing: 0.5px;
    text-transform: uppercase;
  }
</style>
</head>
<body>
  <main class="canvas">
    <section class="business-card">
      <div class="card-frame"></div>
      <h1 class="brand-name">THE COPPER LANTERN</h1>
      <div class="contact-block">
        <p class="person-name">Marco Dellarosa</p>
        <div class="divider divider--wide"></div>
        <address class="address">592 Wexley Street Norfolk<br>Virginia 23847</address>
        <div class="divider divider--narrow"></div>
        <p class="phones">Office: (757) 555-0148<br>Mobile: (757) 555-0193</p>
      </div>
      <p class="tagline">Craft Beer | Upscale Dining Bar<br>Restaurant</p>
    </section>
  </main>
</body>
</html>
```